Career Management Consultant Fun Professional Business Card

This is a business card for a personal career management consultant. The vibe needs to be professional but fun, modern with colour.

The name of the business is "Marcus Telwanger Career Management Consulting"

The name of the individual is "Marcus Telwanger" and his title is "Career Management Consultant"

Industry/Entity Type

Business

Contact Information for Business Card

Marcus Telwanger
Phone: 0400 827 316
Email: Marcus.Telwanger@mailvessa.com

```html
<!DOCTYPE html>
<html lang="en">
<head>
<meta charset="utf-8">
<title>Marcus Telwanger – Business Card</title>
<link rel="stylesheet" href="https://fonts.googleapis.com/css2?family=Montserrat:wght@500&family=Ubuntu:wght@400;500&display=swap">
<style>
  :root {
    --page-bg: #ecebe8;
    --card-bg: #ffffff;
    --brand-blue: #1f6fa8;
    --band-deep: #1d6aa6;
    --band-mid: #4a92cc;
    --rule: #8aa3b8;
    --text-grey: #8a8a8a;
    --text-grey-dark: #7a7a7a;
  }
  * { margin: 0; padding: 0; box-sizing: border-box; }
  html, body {
    width: 967px;
    height: 1200px;
    overflow: hidden;
    background: var(--page-bg);
  }
  .sheet {
    position: relative;
    width: 967px;
    height: 1200px;
  }
  .card {
    position: absolute;
    left: 53px;
    width: 860px;
    height: 490px;
    background: var(--card-bg);
    box-shadow: 0 6px 18px rgba(0,0,0,0.18);
    overflow: hidden;
  }
  .card--front { top: 50px; }
  .card--back { top: 640px; }

  .card__art {
    position: absolute;
    top: 0;
    width: 285px;
    height: 490px;
  }
  .card--front .card__art {
    left: 0;
    background: linear-gradient(90deg, var(--band-deep), var(--band-mid));
  }
  .card--back .card__art {
    right: 0;
    background: linear-gradient(90deg, var(--band-mid), var(--band-deep));
  }

  /* Front */
  .brand-lockup {
    position: absolute;
    left: 360px;
    width: 450px;
    top: 120px;
    text-align: center;
    color: var(--brand-blue);
    font-family: "Montserrat", sans-serif;
    font-weight: 500;
    font-variant: small-caps;
  }
  .brand-lockup__mark {
    display: block;
    width: 62px;
    height: 62px;
    margin: 0 auto 40px;
    background: var(--brand-blue);
  }
  .brand-lockup__name {
    font-size: 40px;
    letter-spacing: 3px;
    line-height: 1;
    padding-bottom: 10px;
    border-bottom: 2px solid var(--rule);
  }
  .brand-lockup__tagline {
    margin-top: 12px;
    font-size: 27px;
    letter-spacing: 2.5px;
    line-height: 1.15;
  }

  /* Back */
  .contact {
    position: absolute;
    left: 32px;
    top: 0;
    font-family: "Ubuntu", sans-serif;
    color: var(--text-grey);
  }
  .contact__name {
    position: absolute;
    top: 58px;
    white-space: nowrap;
    font-size: 44px;
    font-weight: 500;
    color: var(--text-grey-dark);
  }
  .contact__title {
    position: absolute;
    top: 215px;
    white-space: nowrap;
    font-size: 30px;
    font-weight: 400;
  }
  .contact__details {
    position: absolute;
    top: 380px;
    white-space: nowrap;
    font-size: 25px;
    line-height: 1.35;
    list-style: none;
  }
</style>
</head>
<body>
<main class="sheet">
  <section class="card card--front">
    <div class="card__art" role="img" aria-label="Decorative blue and silver wave artwork along the left edge"></div>
    <div class="brand-lockup">
      <span class="brand-lockup__mark"></span>
      <p class="brand-lockup__name">Marcus Telwanger</p>
      <p class="brand-lockup__tagline">Career Management<br>Consulting</p>
    </div>
  </section>

  <section class="card card--back">
    <div class="card__art" role="img" aria-label="Decorative blue and silver wave artwork along the right edge"></div>
    <div class="contact">
      <h1 class="contact__name">Marcus Telwanger</h1>
      <p class="contact__title">Career Management Consultant</p>
      <ul class="contact__details">
        <li>Phone: 0400 827 316</li>
        <li>Email: Marcus.Telwanger@mailvessa.com</li>
      </ul>
    </div>
  </section>
</main>
</body>
</html>
```